Law Firm Letterhead

We are looking for a letterhead for our military/veterans law firm. We like simplicity and clean, modern, flat, uncluttered designs. Our logo font is DIN 1451, and our website/business card info font is Helvetica Neue.

Required Information:

- Logo/Graphic: Please see attached logo / business card for ideas. Please also review firm website.

- Motto: A law firm for service members and veterans

- Web Address: www.brightharborcounsel.example

- Email: info@brightharborcounsel.example

- Phone: 866-214-3097

Colors: We prefer either a blue/grey or an all-blue color scheme. The blue in our logo is #336699.

Please DO NOT submit more than 3 designs. Spamming designs with only minor changes between the designs is not appreciated. We can evaluate your quality and direction by your best 1 or 2 designs.

Thank you!

```html
<!DOCTYPE html>
<html lang="en">
<head>
<meta charset="utf-8">
<title>Bright Harbor Counsel – Letterhead</title>
<link rel="stylesheet" href="https://fonts.googleapis.com/css2?family=EB+Garamond:wght@400;600&display=swap">
<style>
  :root {
    --brand-blue: #336699;
    --paper: #ffffff;
    --band-text: #ffffff;
  }
  html, body {
    margin: 0;
    padding: 0;
    width: 928px;
    height: 1200px;
    overflow: hidden;
    background: var(--paper);
  }
  .letterhead {
    position: relative;
    width: 928px;
    height: 1200px;
    background: var(--paper);
    font-family: "EB Garamond", Garamond, "Times New Roman", serif;
  }
  .firm-name {
    position: absolute;
    left: 0;
    right: 0;
    top: 1060px;
    margin: 0;
    text-align: center;
    color: var(--brand-blue);
    font-size: 27px;
    font-weight: 600;
    letter-spacing: 1px;
    line-height: 1;
    text-transform: uppercase;
  }
  .motto {
    position: absolute;
    left: 0;
    right: 0;
    top: 1096px;
    margin: 0;
    text-align: center;
    color: var(--brand-blue);
    font-size: 20px;
    line-height: 1;
  }
  .footer-band {
    position: absolute;
    left: 0;
    top: 0;
    width: 928px;
    height: 1200px;
  }
  .footer-band .ribbon,
  .footer-band .star { fill: var(--brand-blue); }
  .contact {
    position: absolute;
    top: 1154px;
    margin: 0;
    color: var(--band-text);
    font-size: 15px;
    line-height: 1;
    white-space: nowrap;
  }
  .contact-web { left: 120px; letter-spacing: 3px; }
  .contact-phone { left: 510px; letter-spacing: -0.2px; }
  .contact-email { left: 626px; letter-spacing: -0.2px; }
</style>
</head>
<body>
  <div class="letterhead">
    <p class="firm-name">Bright Harbor Counsel</p>
    <p class="motto">A law firm for service members and veterans</p>

    <svg class="footer-band" viewBox="0 0 928 1200" aria-hidden="true">
      <polygon class="ribbon" points="27,1148 430,1148 440,1161.5 430,1175 27,1175"/>
      <polygon class="ribbon" points="496,1148 900,1148 900,1175 496,1175 488,1161.5"/>
      <polygon class="star" points="464,1127.4 470.2,1146.5 490.3,1146.5 474,1158.3 480.2,1177.3 464,1165.6 447.8,1177.3 454,1158.3 437.7,1146.5 457.8,1146.5"/>
    </svg>

    <p class="contact contact-web">www.brightharborcounsel.example</p>
    <p class="contact contact-phone">866-214-3097</p>
    <p class="contact contact-email">info@brightharborcounsel.example</p>
  </div>
</body>
</html>
```